Business Card Design

Electrical Contracting buisness
need a buisness card relating to that buisness

Reason: Just need to discuss with partner

Industry/Entity Type

Business

Contact Information for Business Card

Dale Fenwick Electrical
0431 756 918
dalefenwick7@mailnest.example
REC 58714

```html
<!DOCTYPE html>
<html lang="en">
<head>
<meta charset="utf-8">
<title>Dale Fenwick Electrical – Business Card</title>
<link rel="stylesheet" href="https://fonts.googleapis.com/css2?family=Open+Sans:wght@400;600;700&display=swap">
<style>
  :root {
    --page-bg: #3a332e;
    --card-top: #1c1c1d;
    --card-bottom: #060606;
    --ink: #f2f2f2;
    --ink-soft: #d6d6d6;
    --accent-orange: #f7941d;
    --accent-red: #e8263a;
    --edge-white: #ffffff;
  }
  * { margin: 0; padding: 0; box-sizing: border-box; }
  html, body {
    width: 1200px;
    height: 855px;
    overflow: hidden;
    background: var(--page-bg);
    font-family: "Open Sans", Arial, sans-serif;
  }
  .canvas {
    width: 1200px;
    height: 855px;
    display: flex;
    align-items: center;
    justify-content: center;
  }
  .business-card {
    position: relative;
    width: 840px;
    height: 480px;
    border-radius: 30px;
    overflow: hidden;
    background: linear-gradient(160deg, var(--card-top) 0%, #111 45%, var(--card-bottom) 100%);
    box-shadow: 0 20px 50px rgba(0,0,0,0.45);
  }
  .card-gloss {
    position: absolute;
    inset: 0;
    background: linear-gradient(125deg, rgba(255,255,255,0.07) 0%, rgba(255,255,255,0.02) 35%, rgba(255,255,255,0) 55%);
  }
  .edge-band {
    position: absolute;
    left: 0; right: 0; bottom: 0;
    height: 14px;
    border-top: 3px solid var(--edge-white);
    background: linear-gradient(90deg, var(--accent-red) 0%, var(--accent-orange) 50%, var(--accent-red) 100%);
  }
  .brand-name {
    position: absolute;
    left: 0; right: 0;
    top: 150px;
    text-align: center;
    color: var(--ink);
    font-weight: 700;
    text-transform: uppercase;
    line-height: 1.05;
  }
  .brand-name .line-main {
    display: block;
    font-size: 62px;
    letter-spacing: 3px;
  }
  .brand-name .line-sub {
    display: block;
    font-size: 36px;
    letter-spacing: 14px;
    margin-top: 8px;
  }
  .contact-list {
    position: absolute;
    left: 56px;
    bottom: 58px;
    list-style: none;
  }
  .contact-item {
    display: flex;
    align-items: center;
    gap: 14px;
    color: var(--ink-soft);
    font-size: 19px;
    margin-top: 16px;
  }
  .contact-icon {
    width: 24px;
    height: 24px;
    flex: none;
  }
  .licence-number {
    position: absolute;
    right: 56px;
    bottom: 58px;
    font-size: 22px;
    color: var(--ink);
    letter-spacing: 0.5px;
  }
  .licence-number .licence-label {
    color: var(--accent-orange);
    font-weight: 700;
    margin-right: 4px;
  }
</style>
</head>
<body>
<main class="canvas">
  <article class="business-card">
    <div class="card-gloss"></div>

    <h1 class="brand-name">
      <span class="line-main">Dale Fenwick</span>
      <span class="line-sub">Electrical</span>
    </h1>

    <ul class="contact-list">
      <li class="contact-item">
        <svg class="contact-icon" viewBox="0 0 24 24" aria-hidden="true">
          <defs>
            <linearGradient id="iconGrad" x1="0" y1="0" x2="0" y2="1">
              <stop offset="0" stop-color="#f7941d"/>
              <stop offset="1" stop-color="#e8263a"/>
            </linearGradient>
          </defs>
          <rect x="0" y="0" width="24" height="24" rx="6" fill="url(#iconGrad)"/>
          <path d="M8.2 6.2c.4-.4 1-.4 1.3 0l1.4 1.7c.3.4.3.9 0 1.2l-.8.8c.6 1.3 1.6 2.4 2.9 3l.8-.8c.3-.3.9-.4 1.2 0l1.7 1.4c.4.3.4.9 0 1.3l-.9.9c-.6.6-1.6.8-2.4.4-2.7-1.2-4.8-3.3-6-6-.4-.8-.2-1.8.4-2.4z" fill="#1a1a1a"/>
        </svg>
        <span>0431 756 918</span>
      </li>
      <li class="contact-item">
        <svg class="contact-icon" viewBox="0 0 24 24" aria-hidden="true">
          <rect x="0" y="0" width="24" height="24" rx="6" fill="url(#iconGrad)"/>
          <rect x="5.5" y="7.5" width="13" height="9" rx="1.2" fill="#1a1a1a"/>
          <path d="M6 8.2l6 4.6 6-4.6" fill="none" stroke="#f7941d" stroke-width="1.2"/>
        </svg>
        <span>dalefenwick7@mailnest.example</span>
      </li>
    </ul>

    <p class="licence-number"><span class="licence-label">REC</span>58714</p>

    <div class="edge-band"></div>
  </article>
</main>
</body>
</html>
```